Corporate holiday party invitation

Please design a holiday party invitations that looks classy and festive for our member holiday party. The event is first class, semi-formal and needs to be conveyed as such. Please see file from last year so you can see what we are aiming for. The new wording for the invite is as follows: (please use similar fonts to the file provided)

Velmora Dallas/Fort Worth
cordially invites you and a guest to the
Yearly Winter Guild Supper Soiree
on Thursday, December 16th
at 6:30pm in the evening

Merrow Tower, Lantern Club
4817 Pell Avenue, 40th floor
Dallas, TX 75288

Tickets are $100 per person and include:
open premium bar, appetizers, three course dinner
and entertainment

Holiday Cocktail Dress

Target Market(s)

middle aged corporate types

Industry/Entity Type

Event

Font styles to use
Script

Requirements
Must have
• Classy holiday feel and design elements,

```html
<!DOCTYPE html>
<html lang="en">
<head>
<meta charset="utf-8">
<title>Velmora Dallas/Fort Worth — Yearly Winter Guild Supper Soiree</title>
<link rel="stylesheet" href="https://fonts.googleapis.com/css2?family=Pinyon+Script&family=Montserrat:wght@400;500;600&display=swap">
<style>
  :root {
    --navy-deep: #0f1930;
    --navy: #1a2847;
    --gold: #d9b25c;
    --gold-soft: #b8924a;
    --gold-dim: rgba(201, 160, 80, 0.22);
    --ivory: #f3efe6;
  }
  * { margin: 0; padding: 0; box-sizing: border-box; }
  html, body {
    width: 849px; height: 1200px; overflow: hidden;
    background: var(--navy-deep);
  }
  .invitation {
    position: relative;
    width: 849px; height: 1200px;
    background: radial-gradient(ellipse at 50% 45%, var(--navy) 0%, var(--navy-deep) 85%);
    overflow: hidden;
  }
  .frame, .dividers {
    position: absolute; inset: 0; width: 849px; height: 1200px;
  }
  .floral {
    position: absolute;
    background: radial-gradient(ellipse at center, var(--gold-dim) 0%, rgba(201,160,80,0.08) 55%, rgba(201,160,80,0) 80%);
  }
  .floral--top-left { left: 34px; top: 34px; width: 140px; height: 150px; }
  .floral--top-right { right: 34px; top: 230px; width: 150px; height: 240px; }
  .floral--left { left: 34px; top: 250px; width: 150px; height: 880px; }
  .floral--bottom-right { right: 34px; top: 520px; width: 150px; height: 620px; }
  .greeting {
    position: absolute; left: 150px; right: 150px; top: 196px;
    text-align: center;
    font-family: "Pinyon Script", cursive;
    font-weight: 400;
    font-size: 38px; line-height: 48px;
    color: var(--gold);
  }
  .details {
    position: absolute; left: 192px; width: 490px;
    font-family: "Montserrat", sans-serif;
    text-transform: uppercase;
    color: var(--ivory);
  }
  .details p { font-size: 23px; line-height: 36px; letter-spacing: 0.6px; white-space: nowrap; }
  .details .accent { color: var(--gold); }
  .when { top: 502px; }
  .where { top: 652px; }
  .tickets { top: 826px; }
  .tickets p { font-size: 16px; line-height: 29px; letter-spacing: 0.4px; }
  .rule {
    position: absolute; left: 192px; width: 480px;
    border: 0; border-top: 2px dashed var(--gold-soft);
  }
  .rule--one { top: 628px; }
  .rule--two { top: 798px; }
  .dress-code {
    position: absolute; left: 203px; top: 1068px; width: 443px; height: 42px;
    border-top: 2px dashed var(--gold-soft);
    border-bottom: 2px dashed var(--gold-soft);
    display: flex; align-items: center; justify-content: center;
    font-family: "Montserrat", sans-serif; font-weight: 500;
    font-size: 17px; letter-spacing: 4px; text-transform: uppercase;
    color: var(--gold);
  }
  .dress-code::before, .dress-code::after {
    content: ""; position: absolute; top: 8px; width: 2px; height: 22px; background: var(--gold-soft);
  }
  .dress-code::before { left: 0; }
  .dress-code::after { right: 0; }
</style>
</head>
<body>
<main class="invitation">
  <svg class="frame" viewBox="0 0 849 1200" aria-hidden="true">
    <rect x="22" y="22" width="805" height="1156" fill="none" stroke="#d9b25c" stroke-width="2"/>
    <rect x="32" y="32" width="785" height="1136" fill="none" stroke="#b8924a" stroke-width="1"/>
  </svg>

  <div class="floral floral--top-left" role="img" aria-label="Gold floral corner ornament"></div>
  <div class="floral floral--top-right" role="img" aria-label="Gold floral scrollwork ornament"></div>
  <div class="floral floral--left" role="img" aria-label="Gold floral vine running down the left edge"></div>
  <div class="floral floral--bottom-right" role="img" aria-label="Gold floral vine running down the right edge"></div>

  <svg class="dividers" viewBox="0 0 849 1200" aria-hidden="true">
    <line x1="290" y1="176" x2="560" y2="176" stroke="#d9b25c" stroke-width="2"/>
    <line x1="320" y1="183" x2="530" y2="183" stroke="#b8924a" stroke-width="1"/>
    <line x1="290" y1="418" x2="560" y2="418" stroke="#d9b25c" stroke-width="2"/>
    <line x1="320" y1="425" x2="530" y2="425" stroke="#b8924a" stroke-width="1"/>
  </svg>

  <h1 class="greeting">
    Velmora Dallas/Fort Worth<br>
    cordially invites you and a guest to the<br>
    Yearly Winter Guild<br>
    Supper Soiree
  </h1>

  <section class="details when">
    <p>On <span class="accent">Thursday, December 16th</span></p>
    <p>at <span class="accent">6:30pm</span> in the <span class="accent">evening</span></p>
  </section>
  <hr class="rule rule--one">

  <section class="details where">
    <p><span class="accent">Merrow Tower</span>, <span class="accent">Lantern Club</span></p>
    <p>4817 Pell Avenue, <span class="accent">40th floor</span></p>
    <p>Dallas, TX 75288</p>
  </section>
  <hr class="rule rule--two">

  <section class="details tickets">
    <p>Tickets are <span class="accent">$100</span> per person and include:</p>
    <p><span class="accent">Open premium bar</span>, appetizers,</p>
    <p>three course dinner and <span class="accent">entertainment</span></p>
  </section>

  <div class="dress-code">Holiday Cocktail Dress</div>
</main>
</body>
</html>
```